a residential painting contractor I need a 6x9 postcard made

I already have a logo, I'm trying to offer my services to people. you can put that there's a 250$ discount for first time customers. include my License number #4629318 as well as the services I offer, interior and exterior painting, pressure washing, cabinet painting, epoxy floors, wood staining, decks, fences and much more. I'm licensed bonded and insured as well.

Target Market(s)

residential consumers (homeowners)

Industry/Entity Type

Painting contractor

Requirements
Must have
• postage stuff on the back I've linked some pictures top right please, my license number, what I do, phone number (341)572-6190 email brushkelvo7@maplint.com, front and back of postcard
Nice to have
• well lit house in the background, maybe little circles of people doing some of the services I offer

```html
<!DOCTYPE html>
<html lang="en">
<head>
<meta charset="utf-8">
<title>Kelvo Painting – 6x9 Postcard</title>
<link rel="stylesheet" href="https://fonts.googleapis.com/css2?family=Tinos:wght@400;700&family=Archivo:wght@700;800&display=swap">
<style>
  :root {
    --stage: #a9a9a9;
    --yellow: #ffcb05;
    --pale-yellow: #ffe78a;
    --cream: #fff6d6;
    --ink: #3f3505;
    --slate: #3b4954;
    --dark-band: #2e3a40;
    --placeholder: #ebebeb;
    --white: #ffffff;
    --black: #111111;
  }
  * { margin: 0; padding: 0; box-sizing: border-box; }
  html, body { width: 901px; height: 1200px; overflow: hidden; }
  body {
    background: var(--stage);
    position: relative;
    font-family: "Tinos", "Times New Roman", serif;
    color: var(--ink);
  }
  .postcard {
    position: absolute;
    left: 92px;
    width: 704px;
    height: 469px;
    overflow: hidden;
    background: var(--yellow);
  }
  .postcard--front { top: 92px; }
  .postcard--back { top: 625px; }
  .postcard__art { position: absolute; inset: 0; width: 704px; height: 469px; }
  .abs { position: absolute; white-space: nowrap; }

  /* front */
  .credentials {
    right: 31px; top: 26px; text-align: right;
    color: var(--slate); font-size: 26px; line-height: 24px;
  }
  .credentials small { font-size: 18px; }
  .offer__amount { left: 222px; top: 340px; font-size: 58px; font-weight: 700; line-height: 1; }
  .offer__label { left: 163px; top: 383px; font-size: 49px; line-height: 1; }
  .offer__who { left: 361px; top: 386px; font-size: 24px; line-height: 19px; }

  .contact { text-align: right; }
  .contact__phone { font-size: 26px; font-weight: 700; line-height: 1; }
  .contact__email { font-size: 15.5px; margin-top: 4px; }
  .contact__license { font-size: 12px; margin-top: 18px; }
  .contact__license b { font-weight: 700; }
  .postcard--front .contact { right: 31px; top: 356px; }
  .postcard--back .contact { left: 176px; top: 354px; text-align: left; }

  .brand { text-align: center; width: 140px; }
  .brand__mark {
    width: 60px; height: 60px; border-radius: 50%;
    background: var(--black); margin: 0 auto 10px;
  }
  .brand__name { font-size: 15px; font-weight: 700; color: var(--black); letter-spacing: .3px; }
  .postcard--front .brand { left: 14px; top: 332px; }
  .postcard--back .brand { left: 14px; top: 336px; }

  /* back */
  .services { left: 44px; top: 48px; color: var(--slate); }
  .services__title { font-size: 25px; font-weight: 700; margin-bottom: 6px; }
  .services__list { list-style: none; font-size: 18px; line-height: 21.5px; }
  .services__list li { display: flex; align-items: baseline; gap: 8px; }
  .services__list svg { flex: none; width: 13px; height: 13px; }
  .services__list li.indent { display: block; padding-left: 21px; }

  .indicia {
    left: 597px; top: 31px; width: 76px; height: 57px;
    border: 1px solid #999; background: var(--white);
    font-family: "Archivo", Arial, sans-serif; font-weight: 700;
    font-size: 8px; line-height: 10.5px; text-align: center; color: var(--black);
    padding-top: 2px;
  }
  .indicia .paid { font-size: 10px; }
  .addressee {
    left: 457px; top: 234px; width: 216px; height: 53px;
    border: 1.5px solid var(--black); background: var(--white);
    font-family: "Archivo", Arial, sans-serif; font-weight: 800;
    font-size: 14.5px; line-height: 19px; color: var(--black);
    padding: 7px 0 0 14px;
  }
</style>
</head>
<body>

<section class="postcard postcard--front">
  <svg class="postcard__art" viewBox="0 0 704 469">
    <defs>
      <linearGradient id="houseScene" x1="0" y1="0" x2="0" y2="1">
        <stop offset="0" stop-color="#c9d3e2"/>
        <stop offset=".55" stop-color="#e8e6e2"/>
        <stop offset="1" stop-color="#8a6b45"/>
      </linearGradient>
    </defs>
    <path d="M0 0 H704 V160 C610 210 470 292 330 292 C200 292 80 245 0 205 Z" fill="var(--cream)"/>
    <path role="img" aria-label="Photo of a well-lit two-storey house at dusk" d="M0 0 H704 V150 C610 200 470 280 330 280 C200 280 80 230 0 196 Z" fill="url(#houseScene)"/>
    <path d="M704 128 V176 C670 200 640 214 610 226 L598 204 C640 180 675 155 704 128 Z" fill="var(--dark-band)"/>
    <path d="M0 230 C120 300 280 320 440 300" fill="none" stroke="#f3bd00" stroke-width="2"/>
    <g>
      <circle cx="401" cy="280" r="41" fill="var(--white)"/>
      <circle role="img" aria-label="Photo of a painter rolling paint onto a wall" cx="401" cy="280" r="38" fill="#7fb0d2"/>
      <circle cx="499" cy="256" r="53" fill="var(--white)"/>
      <circle role="img" aria-label="Photo of hands laying flooring" cx="499" cy="256" r="49" fill="#a9b59a"/>
      <circle cx="619" cy="205" r="68" fill="var(--white)"/>
      <circle role="img" aria-label="Photo of a worker pressure washing a floor" cx="619" cy="205" r="64" fill="#8a8f93"/>
    </g>
  </svg>

  <div class="abs credentials">Licensed bonded<br><small>and</small> Insured</div>

  <div class="abs brand">
    <div class="brand__mark"></div>
    <div class="brand__name">KELVO PAINTING</div>
  </div>

  <div class="abs offer__amount">$250</div>
  <div class="abs offer__label">Discount</div>
  <div class="abs offer__who">new<br>customers</div>

  <div class="abs contact">
    <div class="contact__phone">(341)572-6190</div>
    <div class="contact__email">brushkelvo7@maplint.com</div>
    <div class="contact__license">License Number <b>#4629318</b></div>
  </div>
</section>

<section class="postcard postcard--back">
  <svg class="postcard__art" viewBox="0 0 704 469">
    <path d="M278 -5 C410 150 420 330 350 474" fill="none" stroke="var(--dark-band)" stroke-width="22"/>
    <path d="M300 -5 C432 150 442 330 372 474" fill="none" stroke="var(--pale-yellow)" stroke-width="14"/>
    <path d="M306 -5 C440 150 450 330 378 474 H704 V-5 Z" fill="var(--white)"/>
    <path d="M322 -5 C455 150 465 330 393 474" fill="none" stroke="#d8d8d8" stroke-width="1.2"/>
    <circle cx="335" cy="59" r="41" fill="var(--white)"/>
    <circle cx="335" cy="59" r="38" fill="var(--placeholder)"/>
    <circle cx="367" cy="158" r="52" fill="var(--white)"/>
    <circle cx="367" cy="158" r="48" fill="var(--placeholder)"/>
    <circle cx="379" cy="290" r="66" fill="var(--white)"/>
    <circle cx="379" cy="290" r="62" fill="var(--placeholder)"/>
  </svg>

  <div class="abs services">
    <div class="services__title">Our Services:</div>
    <ul class="services__list">
      <li><svg viewBox="0 0 14 14"><rect x="1" y="3" width="10" height="10" fill="none" stroke="currentColor" stroke-width="1.6"/><path d="M3.5 7.5 L6 10 L13 1.5" fill="none" stroke="currentColor" stroke-width="1.8"/></svg>Interior and exterior painting</li>
      <li><svg viewBox="0 0 14 14"><rect x="1" y="3" width="10" height="10" fill="none" stroke="currentColor" stroke-width="1.6"/><path d="M3.5 7.5 L6 10 L13 1.5" fill="none" stroke="currentColor" stroke-width="1.8"/></svg>Pressure washing</li>
      <li><svg viewBox="0 0 14 14"><rect x="1" y="3" width="10" height="10" fill="none" stroke="currentColor" stroke-width="1.6"/><path d="M3.5 7.5 L6 10 L13 1.5" fill="none" stroke="currentColor" stroke-width="1.8"/></svg>Cabinet painting</li>
      <li><svg viewBox="0 0 14 14"><rect x="1" y="3" width="10" height="10" fill="none" stroke="currentColor" stroke-width="1.6"/><path d="M3.5 7.5 L6 10 L13 1.5" fill="none" stroke="currentColor" stroke-width="1.8"/></svg>Epoxy floors</li>
      <li><svg viewBox="0 0 14 14"><rect x="1" y="3" width="10" height="10" fill="none" stroke="currentColor" stroke-width="1.6"/><path d="M3.5 7.5 L6 10 L13 1.5" fill="none" stroke="currentColor" stroke-width="1.8"/></svg>Wood staining</li>
      <li><svg viewBox="0 0 14 14"><rect x="1" y="3" width="10" height="10" fill="none" stroke="currentColor" stroke-width="1.6"/><path d="M3.5 7.5 L6 10 L13 1.5" fill="none" stroke="currentColor" stroke-width="1.8"/></svg>Decks, fences and</li>
      <li class="indent">much <b>more.</b></li>
    </ul>
  </div>

  <div class="abs brand">
    <div class="brand__mark"></div>
    <div class="brand__name">KELVO PAINTING</div>
  </div>

  <div class="abs contact">
    <div class="contact__phone">(341)572-6190</div>
    <div class="contact__email">brushkelvo7@maplint.com</div>
    <div class="contact__license">License Number <b>#4629318</b></div>
  </div>

  <div class="abs indicia">PRSRT STD<br>ECRWSS<br>U.S.POSTAGE<br><span class="paid">PAID</span><br>EDDM Retail</div>
  <div class="abs addressee">LOCAL POSTAL<br>CUSTOMER</div>
</section>

</body>
</html>
```